Brightwell Power Systems

We'd like a web design that's beautiful and professional. We replace existing inefficient systems (mostly lighting at the moment but expanding) with highly efficient systems.

```html
<!DOCTYPE html>
<html lang="en">
<head>
<meta charset="utf-8">
<title>Brightwell Power Systems</title>
<link rel="stylesheet" href="https://fonts.googleapis.com/css2?family=Ubuntu:wght@300;400;500;700&family=Open+Sans:wght@400;600&display=swap">
<style>
:root{
  --green:#16a85a;
  --green-bright:#1fbf6a;
  --green-band:#14b35e;
  --green-band-mid:#1cbb6c;
  --ink:#2b2b2b;
  --grey-head:#6a6a6a;
  --grey-text:#7a7a7a;
  --link:#1f5a8c;
  --footer-top:#3d3d3d;
  --footer-bottom:#2b2b2b;
  --footer-bar:#222222;
  --footer-text:#a9a9a9;
  --white:#ffffff;
}
*{margin:0;padding:0;box-sizing:border-box}
html,body{width:1150px;height:1200px;overflow:hidden;background:#fff}
body{position:relative;font-family:"Open Sans",Arial,sans-serif;color:var(--grey-text)}
.abs{position:absolute}

/* header */
.topline{left:0;top:0;width:1150px;height:3px;background:var(--green)}
.header{left:0;top:3px;width:1150px;height:69px;background:var(--white)}
.brand{left:145px;top:6px;width:151px;height:127px;background:var(--white);box-shadow:0 2px 8px rgba(0,0,0,.25);border-radius:3px;z-index:5;display:flex;flex-direction:column;align-items:center;justify-content:center;gap:10px}
.brand-mark{width:44px;height:44px;background:var(--green)}
.brand-name{font-family:"Ubuntu",sans-serif;font-weight:500;font-size:15px;line-height:18px;color:var(--green);text-align:center}
.nav{top:36px;font-family:"Ubuntu",sans-serif;font-size:12px;letter-spacing:.5px;color:var(--green)}
.nav svg{vertical-align:middle;margin-left:3px}
.head-social{top:28px;width:25px;height:25px;border:1.5px solid #b9b9b9;border-radius:3px}

/* hero */
.hero{left:0;top:72px;width:1150px;height:419px;
  background:radial-gradient(ellipse 280px 220px at 540px 160px,#f4ffe0 0%,#c8f05a 25%,#7dcf2a 55%,transparent 80%),
  linear-gradient(90deg,#1e6a22 0%,#3ea83a 20%,#78c83a 45%,#5ab936 60%,#2f8a2c 85%,#1d5e20 100%)}
.hero-arrow{top:234px;width:40px;height:40px;border-radius:50%;display:flex;align-items:center;justify-content:center;box-shadow:0 0 0 3px rgba(255,255,255,.25)}
.hero-arrow.prev{left:59px;background:var(--green)}
.hero-arrow.next{left:1053px;background:#3a3a3a}
.hero-title{left:203px;top:306px;width:560px;font-family:"Ubuntu",sans-serif;font-weight:700;font-size:29px;line-height:32px;color:var(--ink);text-shadow:0 1px 2px rgba(255,255,255,.7)}
.hero-sub{left:203px;top:424px;font-family:"Ubuntu",sans-serif;font-weight:500;font-size:16.5px;color:var(--ink);text-shadow:0 1px 2px rgba(255,255,255,.7)}

/* features */
.features{left:0;top:491px;width:1150px;height:163px;background:var(--green-band);display:flex}
.feature{height:163px;display:flex;flex-direction:column;align-items:center;color:var(--white);font-family:"Ubuntu",sans-serif;border-right:1px solid rgba(0,0,0,.08)}
.feature.mid{background:var(--green-band-mid)}
.feature svg{margin-top:22px;height:70px}
.feature h3{font-weight:400;font-size:23px;margin-top:10px}
.feature p{font-size:11px;margin-top:3px}
.band-shadow{left:160px;top:654px;width:830px;height:30px;background:radial-gradient(ellipse at top,rgba(0,0,0,.12),transparent 70%)}

/* content */
.section-title{top:696px;font-family:"Ubuntu",sans-serif;font-size:22px;color:var(--grey-head)}
.photo{top:740px;width:270px;height:112px}
.photo.city{background:linear-gradient(180deg,#2c5cab 0%,#4b86cf 45%,#1c3f7d 100%)}
.photo.pylons{background:linear-gradient(180deg,#8fa6bf 0%,#e9c7a1 60%,#f0b070 78%,#2a2a2a 100%)}
.photo.people{background:linear-gradient(180deg,#e8f0f8 0%,#9fb6cc 50%,#3b5a78 100%)}
.blurb{top:867px;width:270px;font-size:11.5px;line-height:18px;color:var(--grey-text);padding-left:3px}
.learn{top:950px;font-size:11.5px;color:var(--link)}
.news-title{left:730px;top:867px;font-family:"Ubuntu",sans-serif;font-size:15.5px;color:var(--link);text-decoration:underline}
.news-date{left:732px;top:894px;font-size:9.5px;color:#888}
.news-text{left:729px;top:920px;width:265px;font-size:11px;line-height:16px}

/* footer */
.footer{left:0;top:994px;width:1150px;height:165px;background:linear-gradient(180deg,var(--footer-top),var(--footer-bottom))}
.footer-brand{left:154px;top:1020px;width:136px;height:113px;border:2px solid #1a1a1a;display:flex;align-items:center;justify-content:center;gap:8px;padding:6px}
.footer-brand .mark{width:14px;height:14px;background:#0f4a28;flex:none}
.footer-brand span{font-family:"Ubuntu",sans-serif;font-weight:500;font-size:13px;line-height:16px;color:#3a6a48}
.foot-col{top:1022px}
.foot-col h4{font-family:"Ubuntu",sans-serif;font-weight:700;font-size:14px;color:var(--white);margin-bottom:10px}
.foot-col li{list-style:none;font-size:10px;color:var(--footer-text);height:21.5px;display:flex;align-items:center;gap:8px}
.foot-col li .tri{width:0;height:0;border-left:4px solid #888;border-top:3.5px solid transparent;border-bottom:3.5px solid transparent}
.foot-col li.active{color:#2f8fe0}
.contact li{gap:14px;height:27px}
.social-box{top:1053px;width:30px;height:30px;border-radius:3px;background:#5a5a5a;box-shadow:0 2px 3px rgba(0,0,0,.4)}
.footer-bar{left:0;top:1159px;width:1150px;height:41px;background:var(--footer-bar);font-size:10px;color:var(--footer-text)}
.copy{left:141px;top:14px}
.legal{left:873px;top:14px;display:flex;gap:10px}
</style>
</head>
<body>

<div class="abs topline"></div>
<header class="abs header"></header>
<div class="abs brand">
  <div class="brand-mark"></div>
  <div class="brand-name">Brightwell<br>Power Systems</div>
</div>
<nav>
  <span class="abs nav" style="left:497px">HOME</span>
  <span class="abs nav" style="left:581px">ABOUT US<svg width="7" height="5" viewBox="0 0 7 5"><path d="M1 1l2.5 2.5L6 1" fill="none" stroke="#16a85a" stroke-width="1.3"/></svg></span>
  <span class="abs nav" style="left:692px">SERVICES<svg width="7" height="5" viewBox="0 0 7 5"><path d="M1 1l2.5 2.5L6 1" fill="none" stroke="#16a85a" stroke-width="1.3"/></svg></span>
  <span class="abs nav" style="left:801px">CONTACT</span>
</nav>
<div class="abs head-social" style="left:898px"></div>
<div class="abs head-social" style="left:936px"></div>
<div class="abs head-social" style="left:972px"></div>

<section class="abs hero" role="img" aria-label="Rows of green light bulbs hanging from black sockets with one bright glowing bulb in the centre"></section>
<div class="abs hero-arrow prev"><svg width="8" height="10" viewBox="0 0 8 10"><path d="M5.5 1.5L2 5l3.5 3.5" fill="none" stroke="#fff" stroke-width="1.6"/></svg></div>
<div class="abs hero-arrow next"><svg width="8" height="10" viewBox="0 0 8 10"><path d="M2.5 1.5L6 5 2.5 8.5" fill="none" stroke="#fff" stroke-width="1.6"/></svg></div>
<h1 class="abs hero-title">Specialist Services in Electrical Engineering, Energy Management and Power Solutions</h1>
<p class="abs hero-sub">Suspendisse tristique ante sit amet sem pulvinar posuere.</p>

<section class="abs features">
  <div class="feature" style="width:432px">
    <svg width="74" height="72" viewBox="0 0 74 72">
      <rect x="2" y="2" width="70" height="52" fill="#333"/>
      <g stroke="#16b35e" stroke-width="1.3">
        <path d="M2 12h70M2 22h70M2 32h70M2 42h70M16 2v52M30 2v52M44 2v52M58 2v52"/>
      </g>
      <path d="M37 54v10M8 64h30" stroke="#333" stroke-width="2"/>
      <circle cx="7" cy="64" r="3" fill="#333"/>
    </svg>
    <h3>Electrical Installation</h3>
    <p>LOREM IPSUM DOLOR SIT AMET</p>
  </div>
  <div class="feature mid" style="width:287px">
    <svg width="40" height="72" viewBox="0 0 40 72"><path d="M14 2h16l-8 24h14L12 70l6-32H6z" fill="#333"/></svg>
    <h3 style="margin-top:13px">Energy Management</h3>
    <p>LOREM IPSUM DOLOR SIT AMET</p>
  </div>
  <div class="feature" style="width:431px;border-right:none">
    <svg width="72" height="72" viewBox="0 0 72 72">
      <g fill="none" stroke="#333" stroke-width="9">
        <path d="M26 14a26 26 0 0 1 28 6"/>
        <path d="M62 38a26 26 0 0 1-16 24"/>
        <path d="M22 62a26 26 0 0 1-12-26"/>
      </g>
      <path d="M50 10l10 14-16 2z M38 66l-14-2 8-14z M6 28l6-16 10 12z" fill="#333"/>
    </svg>
    <h3 style="margin-top:13px">Renewable Energy</h3>
    <p>LOREM IPSUM DOLOR SIT AMET</p>
  </div>
</section>
<div class="abs band-shadow"></div>

<h2 class="abs section-title" style="left:153px">About Us</h2>
<h2 class="abs section-title" style="left:440px">Our Services</h2>
<h2 class="abs section-title" style="left:727px">Latest News</h2>

<div class="abs photo city" style="left:153px" role="img" aria-label="Blue-toned city skyline with office towers"></div>
<div class="abs photo pylons" style="left:440px" role="img" aria-label="Electricity pylons and power lines against a sunset sky"></div>
<div class="abs photo people" style="left:729px" role="img" aria-label="Silhouetted business people walking in a bright office"></div>

<p class="abs blurb" style="left:153px">Lid est laborum dolo rumes fugats untras. Etharums ser quidem rerum facilis dolores nemis omnis fugats vitaes nemo minima rerums unsers</p>
<p class="abs blurb" style="left:440px">Lid est laborum dolo rumes fugats untras. Etharums ser quidem rerum facilis dolores nemis omnis fugats vitaes nemo minima rerums unsers</p>
<span class="abs learn" style="left:153px">Learn More &nbsp;›</span>
<span class="abs learn" style="left:440px">Learn More &nbsp;›</span>

<a class="abs news-title">The Top 10 Best Electrical Companies</a>
<span class="abs news-date">▦ 8 December 2013</span>
<p class="abs news-text">The point of using Lorem Ipsum is that it has a more-or-less normal distribution of letters, as opposed to using..</p>

<footer class="abs footer"></footer>
<div class="abs footer-brand"><div class="mark"></div><span>Brightwell Power Systems</span></div>

<div class="abs foot-col" style="left:360px">
  <h4>Navigation</h4>
  <ul><li><i class="tri"></i>Home</li><li><i class="tri"></i>About</li><li><i class="tri"></i>Services</li><li><i class="tri"></i>Contact</li></ul>
</div>
<div class="abs foot-col" style="left:504px">
  <h4>Services</h4>
  <ul><li class="active"><i class="tri"></i>Menu1</li><li><i class="tri"></i>Menu1</li><li><i class="tri"></i>Menu1</li><li><i class="tri"></i>Menu1</li></ul>
</div>
<div class="abs foot-col contact" style="left:647px">
  <h4>Contact Us</h4>
  <ul>
    <li><svg width="10" height="12" viewBox="0 0 10 12"><path d="M2 1l2 3-1 1.5c.8 1.8 2 3 3.5 3.5L8 8l2 2-1.5 1.5C5 11 1 6.5.5 2.5z" fill="#888"/></svg>+1800-555-0142</li>
    <li><svg width="11" height="8" viewBox="0 0 11 8"><rect width="11" height="8" fill="#888"/><path d="M0 0l5.5 4.5L11 0" fill="none" stroke="#3a3a3a"/></svg>hello@brightwellpower.com</li>
    <li style="height:24px"><svg width="9" height="12" viewBox="0 0 9 12"><path d="M4.5 0A4.5 4.5 0 0 0 0 4.5C0 8 4.5 12 4.5 12S9 8 9 4.5A4.5 4.5 0 0 0 4.5 0z" fill="#888"/><circle cx="4.5" cy="4.5" r="1.6" fill="#3a3a3a"/></svg>Your Address, Your Country</li>
    <li style="padding-left:23px;height:22px">Your Zip Code</li>
  </ul>
</div>
<div class="abs foot-col" style="left:841px"><h4>Social</h4></div>
<div class="abs social-box" style="left:843px"></div>
<div class="abs social-box" style="left:885px"></div>
<div class="abs social-box" style="left:925px"></div>
<div class="abs social-box" style="left:965px"></div>

<div class="abs footer-bar">
  <span class="abs copy">Copyright 2014 © CompanyName - All Rights Reserved</span>
  <span class="abs legal"><span>Site Map</span><span>•</span><span>Privacy Policy</span></span>
</div>

</body>
</html>
```